Business Card - Cooperate

Business Card for Larkfield Management Consulting

Target Market(s)

Corparte - b2B

Industry/Entity Type

Management Consulting - Professional Services

Contact Information for Business Card

Company Name , Slogan , Dummy Address,

Requirements
Must have
• Reach your Full Potential

```html
<!DOCTYPE html>
<html lang="en">
<head>
<meta charset="utf-8">
<title>Larkfield Management Consulting – Business Card</title>
<link rel="stylesheet" href="https://fonts.googleapis.com/css2?family=Lato:wght@400;700&display=swap">
<style>
  :root {
    --page-bg: #e4e4e4;
    --card-white: #ffffff;
    --card-black: #141414;
    --brand-blue: #2f52ad;
    --name-blue: #2d6ec2;
    --rule-green: #6cbf45;
    --text-dark: #2b2b2b;
    --text-muted: #555555;
    --icon-blue: #3a5fb8;
    --band-light: #1e9bca;
    --band-deep: #2a3f92;
  }
  * { box-sizing: border-box; margin: 0; padding: 0; }
  html, body { width: 1200px; height: 1200px; overflow: hidden; }
  body {
    background: var(--page-bg);
    font-family: "Lato", Arial, sans-serif;
    position: relative;
  }
  .card {
    position: absolute;
    border-radius: 22px;
    overflow: hidden;
  }
  .card-front {
    left: 189px; top: 92px;
    width: 829px; height: 476px;
    background: var(--card-white);
  }
  .card-back {
    left: 187px; top: 639px;
    width: 833px; height: 477px;
    background: var(--card-black);
  }
  .brand {
    position: absolute;
    left: 46px; top: 190px;
    display: flex; align-items: center; gap: 14px;
  }
  .brand-square {
    width: 40px; height: 40px;
    background: var(--brand-blue);
  }
  .brand-name {
    font-weight: 700; font-size: 44px; line-height: 1;
    color: var(--brand-blue);
  }
  .slogan {
    position: absolute;
    left: 46px; top: 256px;
    font-weight: 400; font-size: 17px; line-height: 22px;
    color: var(--text-muted);
  }
  .divider {
    position: absolute;
    left: 414px; top: 127px;
    width: 2px; height: 223px;
    background: var(--rule-green);
  }
  .contact {
    position: absolute;
    left: 458px; top: 126px;
    color: var(--text-dark);
  }
  .person-name {
    font-weight: 700; font-size: 25px; line-height: 30px;
    color: var(--name-blue);
  }
  .person-role { font-size: 19px; line-height: 24px; }
  .address { margin-top: 16px; font-size: 19.5px; line-height: 29px; }
  .details { margin-top: 12px; list-style: none; }
  .details li {
    display: flex; align-items: center; gap: 9px;
    font-size: 19.5px; line-height: 29px;
  }
  .details svg { width: 18px; height: 18px; flex: none; }
  .base-rule {
    position: absolute; left: 0; right: 0; bottom: 62px;
    height: 4px; background: var(--rule-green);
  }
  .base-band {
    position: absolute; left: 0; right: 0; bottom: 0;
    height: 56px;
    background: linear-gradient(90deg, var(--band-light), var(--band-deep));
  }
  .back-pattern {
    position: absolute; inset: 0;
    background: linear-gradient(90deg, #8e8e8e 0%, #5a5a5a 35%, #2c2c2c 70%, #141414 100%);
    opacity: 0.55;
  }
</style>
</head>
<body>
  <section class="card card-front" aria-label="Business card front">
    <div class="brand">
      <span class="brand-square"></span>
      <span class="brand-name">Larkfield</span>
    </div>
    <p class="slogan">Reach your full potential</p>
    <div class="divider"></div>

    <div class="contact">
      <h1 class="person-name">DANIEL AVERY</h1>
      <p class="person-role">President</p>
      <p class="address">2218 Meadow Lane, Brookridge<br>NC 2, United States</p>
      <ul class="details">
        <li>
          <svg viewBox="0 0 24 24" aria-hidden="true"><path fill="var(--icon-blue)" d="M6.6 10.8a15.1 15.1 0 0 0 6.6 6.6l2.2-2.2a1 1 0 0 1 1-.25 11.4 11.4 0 0 0 3.6.57 1 1 0 0 1 1 1V20a1 1 0 0 1-1 1A17 17 0 0 1 3 4a1 1 0 0 1 1-1h3.5a1 1 0 0 1 1 1c0 1.25.2 2.45.57 3.57a1 1 0 0 1-.25 1z"/></svg>
          000-000-000-000
        </li>
        <li>
          <svg viewBox="0 0 24 24" aria-hidden="true"><rect x="2" y="5" width="20" height="14" rx="1" fill="var(--icon-blue)"/><path d="M2.5 5.5 12 13l9.5-7.5M2.5 18.5l7-6.5M21.5 18.5l-7-6.5" stroke="#fff" stroke-width="1.5" fill="none"/></svg>
          info@websitename.com
        </li>
        <li>
          <svg viewBox="0 0 24 24" aria-hidden="true"><g fill="none" stroke="var(--icon-blue)" stroke-width="1.6"><circle cx="12" cy="12" r="9.5"/><ellipse cx="12" cy="12" rx="4.2" ry="9.5"/><path d="M2.5 12h19M4 7h16M4 17h16"/></g></svg>
          www.websitename.com
        </li>
      </ul>
    </div>

    <div class="base-rule"></div>
    <div class="base-band"></div>
  </section>

  <section class="card card-back" aria-label="Business card back">
    <div class="back-pattern" role="img" aria-label="Repeating brand pattern fading from silver on the left to black on the right"></div>
  </section>
</body>
</html>
```